Anzeigengestaltung für Dienstleister für die professionelle Planung und Beschaffung von IT-Lösungen
Zielgruppe
Wir sind Dienstleister für die professionelle Planung und Beschaffung von IT-Lösungen.
Wir bieten umfassende und umfangreiche sowie produktneutrale Beratung zur Umsetzung Ihrer Digitalisierungsprojekte.
Unser Ziel ist es, Ihre individuellen Wünsche und Anforderungen mit speziell auf Sie abgestimmten Konzepten zu realisieren. Hierbei verstehen wir uns als Teamplayer, der alle Aspekte der verschiedenen Fachbereiche zu kombinieren versteht.
Fokus:
Neben den technischen Lösungen erarbeiten wir die detaillierten Anforderungen für Vergabeverfahren (öffentliche Ausschreibung national und EU weit)
Beratung
Planung
Erarbeiten von professionellen und produktneutralen Ausschreibungsunterlagen
Durchführen der Ausschreibung und Vergabe
Professionelle Dokumentation
Professionelle Projektbegleitung bis zur Abnahme und Abrechnung
Bereiche:
Digitalisierung Schulen
Rechenzentren
Telefon Lösungen
Druck Lösungen
Netzwerk und WLAN Lösungen
Zielkunden:
Öffentliche Kunde wie z.B. Kommunen, Schulen, Rathäuser, Hochschulen
Aufgabenstellung
OnePager A4 als Werbeflyer zur Darstellung meines Unternehmen, Neukundengewinnung

```html
<!DOCTYPE html>
<html lang="de">
<head>
<meta charset="utf-8">
<title>Datenbau – Anzeige</title>
<link href="https://fonts.googleapis.com/css2?family=Open+Sans:wght@300;400&display=swap" rel="stylesheet">
<style>
  :root {
    --night: #0a0710;
    --violet: #2c2142;
    --teal: #3fa7c4;
    --ember: #e08a3c;
    --rose: #c46a86;
    --cream: #f3e6cf;
    --lime: #95c11f;
    --white: #ffffff;
    --ink: #3a3a3a;
  }
  html, body {
    margin: 0;
    padding: 0;
    overflow: hidden;
    background: var(--night);
  }
  .ad {
    position: relative;
    width: 849px;
    height: 1200px;
    overflow: hidden;
    font-family: "Open Sans", sans-serif;
    color: var(--white);
    background: var(--night);
  }
  .ad__visual {
    position: absolute;
    inset: 0;
    background:
      radial-gradient(ellipse 120px 90px at 700px 470px, rgba(243,230,207,.18), transparent 70%),
      radial-gradient(ellipse 70px 260px at 570px 720px, rgba(224,138,60,.55), transparent 70%),
      radial-gradient(ellipse 90px 280px at 610px 930px, rgba(196,106,134,.45), transparent 70%),
      radial-gradient(ellipse 110px 240px at 440px 600px, rgba(243,230,207,.55), transparent 70%),
      radial-gradient(ellipse 80px 300px at 440px 160px, rgba(63,167,196,.5), transparent 70%),
      radial-gradient(ellipse 50px 260px at 620px 140px, rgba(243,230,207,.35), transparent 70%),
      radial-gradient(ellipse 320px 260px at 230px 900px, rgba(243,230,207,.16), transparent 70%),
      radial-gradient(ellipse 240px 320px at 220px 260px, rgba(44,33,66,.95), transparent 75%),
      linear-gradient(100deg, transparent 42%, rgba(243,230,207,.10) 52%, rgba(224,138,60,.12) 62%, rgba(196,106,134,.10) 70%, transparent 80%),
      var(--night);
  }
  .services {
    position: absolute;
    left: 66px;
    top: 100px;
    margin: 0;
    padding: 0;
    list-style: none;
    font-size: 20px;
    font-weight: 400;
    letter-spacing: 5px;
    line-height: 37px;
  }
  .band {
    position: absolute;
    left: 0;
    top: 268px;
    width: 849px;
    height: 89px;
    display: flex;
  }
  .band__claim {
    width: 505px;
    background: var(--lime);
    margin: 0;
    padding-left: 67px;
    box-sizing: border-box;
    font-size: 35px;
    font-weight: 300;
    line-height: 89px;
  }
  .band__brand {
    flex: 1;
    background: var(--white);
    display: flex;
    align-items: center;
    justify-content: center;
    gap: 10px;
  }
  .brand__dot {
    width: 18px;
    height: 18px;
    border-radius: 50%;
    background: var(--lime);
  }
  .brand__name {
    color: var(--ink);
    font-size: 32px;
    font-weight: 300;
    letter-spacing: 1px;
  }
  .intro {
    position: absolute;
    left: 73px;
    top: 383px;
    width: 210px;
    font-size: 13px;
    line-height: 17.1px;
    hyphens: auto;
  }
  .intro p { margin: 0 0 17.1px; }
  .imprint {
    position: absolute;
    top: 1085px;
    font-size: 12.5px;
    line-height: 20px;
  }
  .imprint--company { left: 82px; }
  .imprint--contact { left: 241px; }
  .imprint p { margin: 0; }
  .web {
    position: absolute;
    left: 512px;
    top: 1073px;
    font-size: 36px;
    font-weight: 400;
  }
  .foot-bar {
    position: absolute;
    left: 505px;
    top: 1163px;
    width: 344px;
    height: 37px;
    background: var(--lime);
  }
</style>
</head>
<body>
  <main class="ad">
    <div class="ad__visual" role="img" aria-label="Leuchtende Lichtfäden in Türkis, Creme, Orange und Rosa, die sich vor dunklem Hintergrund kreuzen und in Partikel zerstäuben"></div>

    <ul class="services">
      <li>BERATUNG</li>
      <li>PLANUNG</li>
      <li>DURCHFÜHRUNG</li>
      <li>BEGLEITUNG</li>
    </ul>

    <div class="band">
      <h1 class="band__claim">Mit uns in die Zukunft...</h1>
      <div class="band__brand">
        <span class="brand__dot"></span>
        <span class="brand__name">DATENBAU</span>
      </div>
    </div>

    <div class="intro">
      <p>Wir sind Ihr Dienstleister für die professionelle Planung und Beschaffung von IT-Lösungen. Produktneutral und umfassend beraten wir Kommunen, Schulen, Rathäuser und Hochschulen bei ihren Digitalisierungsprojekten – von den Anforderungen bis zur öffentlichen Ausschreibung, national und EU-weit.</p>
      <p>Ausschreibungsunterlagen, Vergabe, Dokumentation und Begleitung bis zur Abnahme und Abrechnung.</p>
      <p>Schulen · Rechenzentren · Telefonie · Druck · Netzwerk &amp; WLAN</p>
    </div>

    <div class="imprint imprint--company">
      <p>Datenbau GmbH</p>
      <p>Lindenallee 14</p>
      <p>88299 Tannweiler</p>
    </div>
    <div class="imprint imprint--contact">
      <p>GF: Jonas Brecht</p>
      <p>Tel: 07500 / 310200-0</p>
      <p>&nbsp;info@datenbau-it.de</p>
    </div>

    <div class="web">datenbau-it.de</div>
    <div class="foot-bar"></div>
  </main>
</body>
</html>
```